ecommerce news podcast artwork

Podcast cover art for a podcast featuring daily news and events around ecommerce product businesses.

text to be: TILLWIRE
optional third line of text with smaller font: Podcast

looking for something that pops with a medium to light blue background. text can be in white/red/orange colors. prefer solid colors for text, but background can vary.
I'm really open to other ideas too, sometimes you don't know what you want until you see it.

Target Market(s)

ecommerce business owners, managers

Industry/Entity Type

news, business, ecommerce

Font styles to use
Sans Serif

Colors
0054AA
0677BA
7BADD7
CADEEF
E8F1F8
0094D4
00A9DD
6FCCEA
C7EBF8
E9F6FB
F0912C
F2A743
F7CA91
FBE8D2
FDF5EE
EB3D1F
EC4F4E
F09395
F8D3D4
FCEDEE

Requirements
Must have
• text: TILLWIRE
Should not have
• no microphones, headsets/headphones, speakers, or other props like that.

```html
<!DOCTYPE html>
<html lang="en">
<head>
<meta charset="utf-8">
<title>TILLWIRE Podcast Cover</title>
<link rel="stylesheet" href="https://fonts.googleapis.com/css2?family=Montserrat:wght@300;800&display=swap">
<style>
  :root {
    --page-bg: #ffffff;
    --cover-glow: #0650d8;
    --cover-mid: #06369a;
    --cover-deep: #04204f;
    --cover-edge: #020f24;
    --title-ink: #ffffff;
    --title-shadow: rgba(0, 8, 30, 0.75);
  }
  html, body {
    margin: 0;
    padding: 0;
    width: 1200px;
    height: 1000px;
    overflow: hidden;
    background: var(--page-bg);
  }
  .canvas {
    position: relative;
    width: 1200px;
    height: 1000px;
  }
  .cover {
    position: absolute;
    left: 242px;
    top: 144px;
    width: 720px;
    height: 720px;
    background:
      radial-gradient(circle at 42% 33%, var(--cover-glow) 0%, var(--cover-mid) 30%, var(--cover-deep) 62%, var(--cover-edge) 100%);
  }
  .cover-title {
    position: absolute;
    left: 0;
    top: 0;
    width: 1200px;
    height: 1000px;
    overflow: visible;
  }
  .title-word {
    fill: var(--title-ink);
    font-family: "Montserrat", sans-serif;
    filter: drop-shadow(4px 5px 5px var(--title-shadow));
  }
  .title-word--bold {
    font-weight: 800;
    font-size: 192px;
    letter-spacing: 2px;
  }
  .title-word--light {
    font-weight: 300;
    font-size: 202px;
    letter-spacing: 0;
  }
</style>
</head>
<body>
  <main class="canvas">
    <section class="cover" aria-label="TILLWIRE podcast cover"></section>
    <svg class="cover-title" viewBox="0 0 1200 1000" role="img" aria-label="TILLWIRE">
      <text class="title-word title-word--bold" x="314" y="497">TILL</text>
      <text class="title-word title-word--light" x="304" y="647">WIRE</text>
    </svg>
  </main>
</body>
</html>
```